Local Flower Farm Needs Business Card Design

I need business cards designed for a flower farm based in Eudora, Kansas.
Business Info:
We are a local cut flower farm located in Eudora, Kansas, founded by Darla Hoffstrom. What started as a passion for agriculture and search for more joy in daily life has blossomed into a small business dedicated to providing the community with beautiful, fresh, and sustainable flowers. We specialize in local, seasonal blooms, ensuring that every petal reflects the care and dedication we pour into our craft. Our mission is to deliver the highest quality flowers directly to our customers through local farmers markets and to florists who share our commitment to sustainability. Join us in celebrating the beauty of nature, one bloom at a time!
Contact Details:
Darla Hoffstrom
Owner
Phone 913-555-0147
Facebook: Lorabelle Quinn Blossoms
Instagram: @LorabelleQuinnBlossoms
Website: LorabelleQuinnBlossoms.example
Target Market(s)
Wholesale to Florists and Direct to Consumer via Farmers Market
Industry/Entity Type
Florist, Farm
Contact Information for Business Card
Name, Contact Info, Logo
Look and feel

```html
<!DOCTYPE html>
<html lang="en">
<head>
<meta charset="utf-8">
<title>Lorabelle Quinn Blossoms — Business Card</title>
<link rel="stylesheet" href="https://fonts.googleapis.com/css2?family=Libre+Caslon+Text:wght@400&display=swap">
<style>
  :root {
    --page-bg: #d9d3cb;
    --card-light-top: #f1efeb;
    --card-light-bottom: #e2e6ea;
    --band-dark: #1f2a2f;
    --band-dark-edge: #162025;
    --ink: #1c2529;
    --muted-text: #b9a9a4;
    --seal-fill: #eeebe8;
    --seal-line: #1c2529;
  }
  * { box-sizing: border-box; margin: 0; padding: 0; }
  html, body {
    width: 1200px; height: 970px; overflow: hidden;
    background: var(--page-bg);
    font-family: "Libre Caslon Text", Georgia, serif;
  }
  .business-card {
    position: absolute; left: 75px; top: 185px;
    width: 1050px; height: 600px;
    background: linear-gradient(180deg, var(--card-light-top), var(--card-light-bottom));
    box-shadow: 0 18px 40px rgba(40, 30, 20, 0.25);
    overflow: hidden;
  }
  .contact-band {
    position: absolute; left: 0; right: 0; top: 297px; bottom: 0;
    background: linear-gradient(180deg, var(--band-dark), var(--band-dark-edge));
  }
  .owner {
    position: absolute; left: 54px; top: 62px; color: var(--ink);
  }
  .owner-name {
    font-size: 34px; letter-spacing: 1.5px; text-transform: uppercase; line-height: 1.1;
  }
  .owner-title { font-size: 23px; margin-top: 6px; letter-spacing: 0.5px; }
  .brand-seal {
    position: absolute; left: 525px; top: 300px;
    width: 330px; height: 330px; margin: -165px 0 0 -165px;
    border-radius: 50%;
    background: var(--seal-fill);
    display: flex; align-items: center; justify-content: center;
  }
  .brand-seal::after {
    content: ""; position: absolute; inset: 14px;
    border: 1.5px solid var(--seal-line); border-radius: 50%;
  }
  .brand-name {
    font-size: 30px; line-height: 1.25; color: var(--ink);
    text-align: center; width: 220px;
  }
  .contact-list {
    position: absolute; top: 478px; list-style: none;
    font-size: 24px; color: var(--muted-text);
  }
  .contact-list li {
    display: flex; align-items: center; gap: 14px; height: 35px;
  }
  .contact-left { left: 54px; }
  .contact-right { right: 52px; }
  .contact-right li { justify-content: flex-end; }
  .contact-icon { width: 30px; height: 30px; flex: none; }
  .social-dot {
    width: 28px; height: 28px; border-radius: 50%;
    border: 1.5px solid var(--muted-text); flex: none;
  }
</style>
</head>
<body>
  <main class="business-card">
    <div class="contact-band"></div>

    <header class="owner">
      <h1 class="owner-name">Darla Hoffstrom</h1>
      <p class="owner-title">Owner</p>
    </header>

    <div class="brand-seal">
      <p class="brand-name">Lorabelle Quinn Blossoms</p>
    </div>

    <ul class="contact-list contact-left">
      <li>
        <svg class="contact-icon" viewBox="0 0 30 30" aria-hidden="true">
          <circle cx="15" cy="15" r="13.5" fill="none" stroke="#b9a9a4" stroke-width="1.5"/>
          <path d="M11 8.5c-1.2.6-2 1.8-1.5 3.6 1 3.6 4 7.4 7.6 8.8 1.6.6 2.9 0 3.6-1.2l-2.4-2.2-1.6 1c-1.8-.9-3.3-2.6-4-4.4l1.4-1.2z" fill="#b9a9a4"/>
        </svg>
        <span>913-555-0147</span>
      </li>
      <li>
        <svg class="contact-icon" viewBox="0 0 30 30" aria-hidden="true">
          <g fill="none" stroke="#b9a9a4" stroke-width="1.3">
            <circle cx="15" cy="15" r="13.5"/>
            <circle cx="15" cy="15" r="8"/>
            <ellipse cx="15" cy="15" rx="3.5" ry="8"/>
            <path d="M7 15h16M8.5 11h13M8.5 19h13"/>
          </g>
        </svg>
        <span>LorabelleQuinnBlossoms.example</span>
      </li>
    </ul>

    <ul class="contact-list contact-right">
      <li><span>Lorabelle Quinn Blossoms</span><span class="social-dot"></span></li>
      <li><span>@LorabelleQuinnBlossoms</span><span class="social-dot"></span></li>
    </ul>
  </main>
</body>
</html>
```